Business card - mobile service

O KiraTel is a mobile family safety service based on tablets and smartphones.
The business card must have:
BASIC INFO
Company Logo
Name
Position / Job Title: Co-founder
Mobile Phone Number: +55 (11) 5080 6172
Land Line: +55 (11) 9087 614352
Email Address: name@kiratel-example.com
Web Site URL: www.kiratel-example.com
PROMOTIONAL INFO
Try KiraTel free Today!
Your personal promo code: xxxx-2222-uuuu-7777-1234
Promo code text explanation with the instructions about the trial offer
Updates
Dears,
One more must have: the KiraTel slogan:
Industry/Entity Type
Safety
Look and feel
Each slider illustrates characteristics of the customer's brand and the style your logo design should communicate.

```html
<!DOCTYPE html>
<html lang="en">
<head>
<meta charset="utf-8">
<title>KiraTel business card</title>
<link rel="stylesheet" href="https://fonts.googleapis.com/css2?family=Source+Sans+3:wght@400;600;700&family=Fredoka:wght@600&display=swap">
<style>
  :root {
    --paper: #ffffff;
    --card-top: #fbfaf6;
    --card-bottom: #e9e4d6;
    --brand-blue: #29a9e1;
    --brand-yellow: #f6c319;
    --bubble-top: #7fbdf0;
    --bubble-bottom: #1d5fae;
    --blob-top: #5d9be0;
    --blob-bottom: #15479a;
    --promo-yellow: #f3e11a;
    --slogan-orange: #f7931e;
    --ink: #1a1a1a;
    --white: #ffffff;
  }
  * { margin: 0; padding: 0; box-sizing: border-box; }
  html, body {
    width: 1200px; height: 900px; overflow: hidden;
    background: var(--paper);
    font-family: "Source Sans 3", "Myriad Pro", Arial, sans-serif;
  }
  .card {
    position: absolute; left: 272px; width: 654px; height: 378px;
    background: linear-gradient(to bottom, var(--card-top) 0%, var(--card-bottom) 100%);
    overflow: hidden;
  }
  .card--front { top: 40px; }
  .card--back { top: 474px; height: 380px; }

  .wordmark {
    position: absolute;
    font-family: "Source Sans 3", Arial, sans-serif;
    font-weight: 700; color: var(--brand-blue);
    display: flex; align-items: center; gap: 10px;
    letter-spacing: -1px;
  }
  .wordmark__dot {
    width: 22px; height: 22px; border-radius: 50%;
    background: var(--brand-yellow);
  }
  .card--front .wordmark { left: 52px; top: 82px; font-size: 74px; }
  .card--back .wordmark { left: 418px; top: 96px; font-size: 62px; }

  .identity {
    position: absolute; right: 30px; top: 0; text-align: right; color: var(--ink);
  }
  .identity__name { margin-top: 36px; font-size: 28px; font-weight: 400; line-height: 1.1; }
  .identity__role { font-size: 19px; line-height: 1.2; }

  .phones {
    position: absolute; right: 30px; top: 244px; text-align: right;
    font-size: 17px; line-height: 24px; color: var(--ink);
  }

  .band {
    position: absolute; left: 0; right: 0; bottom: 0;
    background: var(--brand-blue); color: var(--white);
    display: flex; flex-direction: column; align-items: center; justify-content: center;
  }
  .card--front .band { height: 76px; font-size: 20px; line-height: 28px; }
  .card--back .band { height: 76px; }

  .slogan {
    font-family: "Fredoka", "Arial Rounded MT Bold", sans-serif;
    font-weight: 600; font-size: 36px; color: var(--slogan-orange);
    -webkit-text-stroke: 1.5px var(--white);
    paint-order: stroke fill;
    text-shadow: 0 0 2px var(--white), 0 0 3px var(--white);
  }

  .promo { position: absolute; left: 0; top: 0; width: 654px; height: 302px; }
  .promo text { font-family: "Source Sans 3", Arial, sans-serif; }
</style>
</head>
<body>

<section class="card card--front">
  <div class="wordmark"><span class="wordmark__dot"></span>KiraTel</div>
  <div class="identity">
    <p class="identity__name">employee name</p>
    <p class="identity__role">Co-founder</p>
  </div>
  <div class="phones">
    <p>Mobile Phone Number: +55 (11) 5080 6172</p>
    <p>Land Line: +55 (11) 9087 614352</p>
  </div>
  <div class="band">
    <p>email: name@kiratel-example.com</p>
    <p>web: www.kiratel-example.com</p>
  </div>
</section>

<section class="card card--back">
  <svg class="promo" viewBox="0 0 654 302" xmlns="http://www.w3.org/2000/svg">
    <defs>
      <linearGradient id="bubbleFill" x1="0" y1="0" x2="0" y2="1">
        <stop offset="0" stop-color="var(--bubble-top)"/>
        <stop offset="1" stop-color="var(--bubble-bottom)"/>
      </linearGradient>
      <linearGradient id="blobFill" x1="0" y1="0" x2="0" y2="1">
        <stop offset="0" stop-color="var(--blob-top)"/>
        <stop offset="1" stop-color="var(--blob-bottom)"/>
      </linearGradient>
    </defs>

    <g class="try-bubble">
      <path d="M44 38 Q28 38 26 58 L22 116 Q22 134 34 138 L30 176 L62 142 L180 146 Q196 146 198 128 L200 52 Q200 34 182 34 Z"
            fill="url(#bubbleFill)" stroke="#0f3f7a" stroke-width="2"/>
      <path d="M46 44 L180 40 Q192 40 192 52 L190 76 Q120 64 32 86 L34 58 Q36 44 46 44 Z" fill="#ffffff" opacity="0.25"/>
      <text x="60" y="74" fill="var(--white)" font-size="18">Try</text>
      <text x="58" y="102" fill="var(--promo-yellow)" font-size="27" font-weight="600">KiraTel</text>
      <text x="86" y="126" fill="var(--white)" font-size="17">free Today!</text>
    </g>

    <g class="code-blob">
      <path d="M110 152 Q80 156 80 198 Q78 252 160 256 Q260 262 340 252 Q432 244 424 194 Q418 158 360 160 Q300 162 240 150 Q170 140 110 152 Z"
            fill="url(#blobFill)" stroke="#0f3f7a" stroke-width="2"/>
      <path d="M112 158 Q160 148 240 158 Q300 168 360 166 Q404 166 412 186 Q300 196 90 196 Q92 164 112 158 Z" fill="#ffffff" opacity="0.18"/>
      <text x="256" y="190" text-anchor="middle" fill="var(--white)" font-size="14">Your personal promo code:</text>
      <text x="256" y="208" text-anchor="middle" fill="var(--white)" font-size="13">xxxx-2222-uuuu-7777-1234</text>
      <text x="252" y="232" text-anchor="middle" fill="var(--promo-yellow)" font-size="12.5">Promo code text explanation with the</text>
      <text x="252" y="248" text-anchor="middle" fill="var(--promo-yellow)" font-size="12.5">instructions about the trial offer</text>
    </g>
  </svg>

  <div class="wordmark"><span class="wordmark__dot"></span>KiraTel</div>

  <div class="band">
    <p class="slogan">Your Family Safety Service</p>
  </div>
</section>

</body>
</html>
```